Fresh Start Bold Body Challenge 2017 Poster

We are having a Fresh Start, Bold Body Challenge for 2017 at our fitness studio. We need a poster design using the template attached as a reference (Only reference). I have also included our Vorbelix logo to put on the poster. Please DO NOT use the graphics in the flyer as we are expecting something much much better :-)
MUST HAVES:
- Size needed 11x17 with bleeding for printing
- .PSD File Format WITH LAYERS (CS3 Compatible)*** A MUST
- Use Vorbelix Bootcamps Logo
- Use Information in the attached word doc

```html
<!DOCTYPE html>
<html lang="en">
<head>
<meta charset="utf-8">
<title>Fresh Start, Bold Body Challenge 2017 – Vorbelix Bootcamps</title>
<link rel="stylesheet" href="https://fonts.googleapis.com/css2?family=Oswald:wght@500;700&family=Dosis:wght@600;700&family=Open+Sans:wght@400;800&display=swap">
<style>
:root{
  --bg-dark:#161616;
  --bg-mid:#2a2a2a;
  --white:#ffffff;
  --orange:#f7941d;
  --rule:#3f74b8;
  --band:#3d88c9;
  --band-text:#14233b;
}
*{margin:0;padding:0;box-sizing:border-box}
html,body{width:776px;height:1200px;overflow:hidden;background:var(--bg-dark)}
.poster{
  position:relative;width:776px;height:1200px;overflow:hidden;
  background:radial-gradient(ellipse at 50% 45%,var(--bg-mid) 0%,#1f1f1f 55%,var(--bg-dark) 100%);
  font-family:"Oswald",sans-serif;color:var(--white);
}
.hero-photos{
  position:absolute;left:0;top:0;width:776px;height:220px;
  background:linear-gradient(90deg,#3a3a3a 0%,#5c5c5c 30%,#6f6f6f 55%,#4c4c4c 80%,#2e2e2e 100%);
}
.hero-photos::after{
  content:"";position:absolute;inset:0;
  background:linear-gradient(180deg,rgba(22,22,22,0) 55%,rgba(22,22,22,.95) 100%);
}
.hero-dividers{position:absolute;left:0;top:0}
.headline{
  position:absolute;left:0;top:172px;width:776px;text-align:center;
  font-weight:700;text-transform:uppercase;line-height:80px;font-size:88px;letter-spacing:1px;
  text-shadow:0 3px 6px rgba(0,0,0,.6);
}
.headline .accent{color:var(--orange);display:block;margin-top:22px}
.tagline{
  position:absolute;left:0;top:546px;width:776px;text-align:center;
  font-weight:700;font-size:27px;line-height:40px;
}
.details{
  position:absolute;left:120px;top:660px;width:532px;height:288px;
  border-top:1px solid var(--rule);border-bottom:1px solid var(--rule);
}
.details::before,.details::after{
  content:"";position:absolute;top:12px;bottom:12px;width:1px;background:var(--rule);
}
.details::before{left:5px}
.details::after{right:5px}
.schedule{
  position:absolute;left:30px;top:26px;
  font-family:"Dosis",sans-serif;font-weight:600;font-size:20px;line-height:23px;
  display:grid;grid-template-columns:180px auto;
}
.schedule dt{color:var(--orange)}
.schedule dd{color:var(--white)}
.split-rule{position:absolute;left:8px;right:8px;top:152px;height:1px;background:var(--rule)}
.offer{position:absolute;left:18px;top:175px;width:250px;height:100px}
.offer-note{
  font-family:"Oswald",sans-serif;font-weight:500;color:var(--orange);
  font-size:15px;line-height:21px;
}
.offer-price{
  position:absolute;left:126px;top:34px;font-family:"Open Sans",sans-serif;
  font-weight:800;font-size:38px;line-height:40px;color:var(--white);
}
.offer-split{position:absolute;left:278px;top:170px;width:1px;height:110px;background:var(--rule)}
.prize{position:absolute;left:285px;top:172px;width:247px;text-align:center}
.prize-amount{font-family:"Open Sans",sans-serif;font-weight:800;font-size:42px;line-height:50px}
.prize-note{color:var(--orange);font-weight:500;font-size:21px;line-height:26px}
.brand{
  position:absolute;left:0;top:1020px;width:776px;text-align:center;
  display:flex;justify-content:center;align-items:center;gap:14px;
  font-family:"Oswald",sans-serif;font-weight:700;font-size:40px;text-transform:uppercase;color:var(--white);
}
.brand-mark{width:26px;height:26px;background:var(--orange)}
.info-band{
  position:absolute;left:0;top:1120px;width:776px;height:80px;background:var(--band);
  display:flex;justify-content:center;align-items:center;gap:8px;
  font-family:"Open Sans",sans-serif;color:var(--band-text);font-size:20px;letter-spacing:.5px;
}
.info-band .url{font-weight:800;font-size:25px;letter-spacing:0}
</style>
</head>
<body>
<main class="poster">
  <div class="hero-photos" role="img" aria-label="Three black-and-white photos of bootcamp members training: flipping a tyre, doing plank exercises, and working with battle ropes"></div>
  <svg class="hero-dividers" width="776" height="220" viewBox="0 0 776 220" aria-hidden="true">
    <line x1="260" y1="0" x2="215" y2="220" stroke="#3f74b8" stroke-width="2"/>
    <line x1="660" y1="0" x2="625" y2="220" stroke="#3f74b8" stroke-width="2"/>
  </svg>

  <h1 class="headline">Fresh Start,<br>Bold Body<span class="accent">Challenge</span></h1>

  <p class="tagline">In just 6 weeks, transform your body and<br>get in the best shape of your life!</p>

  <section class="details">
    <dl class="schedule">
      <dt>Kick Off Meeting:</dt><dd>Thursday, Jan 12th at 7:30 pm</dd>
      <dt>Start Date:</dt><dd>Tuesday, January 17th</dd>
      <dt>End Date:</dt><dd>Saturday, February 25th</dd>
      <dt>Finale Party :</dt><dd>March 2nd</dd>
    </dl>
    <div class="split-rule"></div>
    <div class="offer">
      <p class="offer-note">6 Weeks of Training, Nutrition,<br>and Coaching<br>Starting at just</p>
      <p class="offer-price">$99!</p>
    </div>
    <div class="offer-split"></div>
    <div class="prize">
      <p class="prize-amount">$500</p>
      <p class="prize-note">Cash Prize for Winner!</p>
    </div>
  </section>

  <div class="brand"><span class="brand-mark"></span><span>Vorbelix Bootcamps</span></div>

  <footer class="info-band">
    <span>VISIT</span><span class="url">www.vorbelixbootcamps.com</span><span>FOR MORE INFO</span>
  </footer>
</main>
</body>
</html>
```